Post Card Design Bright Lantern Youth

We need a postcard design that will be mailed to all residents offering free pickups of donated clothing. Our foundation is called Bright Lantern Youth, we are a nonprofit charitable organization that provides meals and medical services to children in need in Honduras. Collecting unwanted second-hand clothing generates revenue that helps fund the mission and programs run by our foundation. We would like to offer our pickup services to everyone who has any unwanted reusable clothing.

```html
<!DOCTYPE html>
<html lang="en">
<head>
<meta charset="UTF-8">
<title>Bright Lantern Youth – Free Pickup Postcard</title>
<link href="https://fonts.googleapis.com/css2?family=Source+Sans+3:ital,wght@0,600;0,700;1,600&display=swap" rel="stylesheet">
<style>
  :root {
    --slate: #4f6a63;
    --slate-dark: #435d58;
    --mist: #a9b5b0;
    --panel-bg: #e9ebea;
    --white: #ffffff;
    --brand-green: #7cc242;
    --rule-green: #7dbb2e;
    --olive: #7c7b3c;
    --teal: #2a5c61;
    --ink: #111111;
    --footer-start: #7dc142;
    --footer-end: #2c6a6a;
  }
  * { margin: 0; padding: 0; box-sizing: border-box; }
  html, body { width: 800px; height: 1200px; overflow: hidden; background: var(--white); }
  body { font-family: "Source Sans 3", "Myriad Pro", sans-serif; }
  .postcard { position: relative; width: 800px; height: 1200px; overflow: hidden; background: var(--panel-bg); }

  .hero {
    position: absolute; left: 0; top: 0; width: 800px; height: 690px;
    background: linear-gradient(90deg, var(--mist) 0%, #7c8f89 38%, var(--slate) 60%, var(--slate-dark) 100%);
  }
  .hero-photo {
    position: absolute; left: 0; top: 0; width: 330px; height: 690px;
    background: radial-gradient(ellipse at 45% 45%, #5a4a40 0%, #3b3733 25%, #d9d7cf 42%, #a3aea9 70%, #7f918b 100%);
  }
  .hero-shapes { position: absolute; left: 0; top: 0; }

  .brand { position: absolute; right: 34px; top: 56px; width: 330px; text-align: center; }
  .brand-mark { display: block; width: 36px; height: 36px; border-radius: 50%; background: var(--brand-green); margin: 0 auto 10px; }
  .brand-name { font-size: 34px; font-weight: 700; color: var(--brand-green); line-height: 1; }

  .headline { position: absolute; left: 340px; top: 206px; color: var(--white); font-weight: 700; }
  .headline-main { font-size: 67px; line-height: 1; letter-spacing: 0.5px; }
  .headline-sub { font-size: 35px; line-height: 1; margin-top: 10px; }
  .headline-rule { position: absolute; left: 340px; top: 324px; width: 414px; height: 5px; border-radius: 3px; background: var(--rule-green); }

  .intro { position: absolute; left: 341px; top: 346px; width: 430px; color: var(--white); font-size: 23px; font-weight: 600; line-height: 30px; }
  .intro p + p { margin-top: 29px; }

  .about-card {
    position: absolute; left: 34px; top: 709px; width: 365px; height: 326px;
    background: var(--white); border-radius: 22px; padding: 78px 20px 0 17px;
  }
  .tag {
    position: absolute; display: inline-block; background: var(--olive); color: var(--white);
    font-style: italic; font-weight: 600; font-size: 20px; line-height: 32px; padding: 0 13px; border-radius: 16px;
  }
  .about-card .tag { left: 14px; top: 15px; }
  .about-card p { font-size: 20.5px; font-weight: 600; line-height: 27px; color: var(--ink); }
  .about-card p + p { margin-top: 27px; }

  .steps { position: absolute; left: 420px; top: 720px; width: 360px; }
  .steps .tag { left: 0; top: 0; }
  .step { position: absolute; left: 2px; display: flex; align-items: flex-start; }
  .step-num {
    flex: none; width: 45px; height: 45px; border-radius: 50%; background: var(--teal); color: var(--white);
    font-size: 31px; font-weight: 700; line-height: 45px; text-align: center;
  }
  .step-text { margin-left: 15px; font-size: 21px; font-weight: 600; line-height: 27px; color: var(--ink); }
  .step-1 { top: 52px; } .step-1 .step-text { padding-top: 5px; }
  .step-2 { top: 126px; } .step-2 .step-text { padding-top: 2px; }
  .step-3 { top: 200px; } .step-3 .step-text { padding-top: 2px; }

  .footer {
    position: absolute; left: 0; top: 1052px; width: 800px; height: 148px;
    background: linear-gradient(90deg, var(--footer-start) 0%, #52954b 55%, var(--footer-end) 100%);
    color: var(--white);
  }
  .footer-label { position: absolute; left: 24px; top: 24px; font-size: 20px; font-weight: 700; }
  .footer-phone { position: absolute; left: 22px; top: 46px; font-size: 58px; font-weight: 700; line-height: 1.1; }
  .footer-web { position: absolute; left: 26px; top: 113px; font-size: 22px; font-style: italic; font-weight: 600; opacity: 0.9; }
  .clothing-art {
    position: absolute; left: 452px; top: 12px; width: 292px; height: 122px; border-radius: 14px;
    background: linear-gradient(90deg, #c9b3d8 0%, #f6b6ae 35%, #ef8e72 55%, #a9d6cf 75%, #f3e7c7 100%);
    opacity: 0.85;
  }
</style>
</head>
<body>
<main class="postcard">
  <section class="hero">
    <div class="hero-photo" role="img" aria-label="Photograph of a young girl looking out through a torn opening in a white tarp shelter"></div>
    <svg class="hero-shapes" width="800" height="690" viewBox="0 0 800 690" aria-hidden="true">
      <path d="M352 0 C 372 95, 420 160, 520 164 L 800 166 L 800 0 Z" fill="#ffffff"/>
      <path d="M0 668 C 180 690, 300 650, 480 648 C 620 646, 720 665, 800 680 L 800 690 L 0 690 Z" fill="#e9ebea"/>
    </svg>
    <div class="brand">
      <span class="brand-mark"></span>
      <span class="brand-name">Bright Lantern Youth</span>
    </div>
    <h1 class="headline">
      <div class="headline-main">FREE PICKUP</div>
      <div class="headline-sub">OF DONATED CLOTHING!</div>
    </h1>
    <div class="headline-rule"></div>
    <div class="intro">
      <p>We are a nonprofit charitable organization that provides meals and medical services to children in need in Honduras. Your donated clothing helps fund our mission and programs.</p>
      <p>By donating your unwanted reusable clothing, you are directly supporting our efforts to make a difference.</p>
    </div>
  </section>

  <section class="about-card">
    <span class="tag">More About Us:</span>
    <p>Bright Lantern Youth collects unwanted second-hand clothing to generate revenue that helps fund our programs.</p>
    <p>We rely on the generosity of our community to provide essential services to children in need.</p>
  </section>

  <section class="steps">
    <span class="tag">How to Schedule a Pickup:</span>
    <div class="step step-1"><span class="step-num">1</span><span class="step-text">Call or visit our website.</span></div>
    <div class="step step-2"><span class="step-num">2</span><span class="step-text">Schedule a date and<br>time convenient for you.</span></div>
    <div class="step step-3"><span class="step-num">3</span><span class="step-text">Place your donated clothing<br>outside, and we’ll handle<br>the rest!</span></div>
  </section>

  <footer class="footer">
    <div class="footer-label">Contact Us for Free pickup:</div>
    <div class="footer-phone">(000)-000-0000</div>
    <div class="footer-web">www.brightlanternyouth.org</div>
    <div class="clothing-art" role="img" aria-label="Illustration of children's clothing: overalls, dresses, a romper, a t-shirt, socks and trousers"></div>
  </footer>
</main>
</body>
</html>
```